The Larchmont Fitters

We need a business card design for our wardrobe company.
Please visit our website www.glimmerbayinteriors.com to get an idea of who we are.

```html
<!DOCTYPE html>
<html lang="en">
<head>
<meta charset="utf-8">
<title>The Larchmont Fitters — Business Card</title>
<link rel="stylesheet" href="https://fonts.googleapis.com/css2?family=Open+Sans:wght@400;600;700&display=swap">
<style>
  :root {
    --stage: #e4e4e4;
    --card-white: #ffffff;
    --card-black: #050505;
    --ink: #111111;
    --ink-soft: #333333;
    --paper-text: #ffffff;
  }
  * { box-sizing: border-box; margin: 0; padding: 0; }
  html, body {
    width: 1200px; height: 900px; overflow: hidden;
    background: var(--stage);
    font-family: "Open Sans", Arial, sans-serif;
  }
  .stage {
    position: relative; width: 1200px; height: 900px;
    display: flex; align-items: center; justify-content: center; gap: 50px;
  }
  .card {
    position: relative; width: 525px; height: 300px;
    box-shadow: 0 6px 18px rgba(0,0,0,0.12);
    overflow: hidden;
  }
  .card--front { background: var(--card-white); color: var(--ink); }
  .card--back { background: var(--card-black); color: var(--paper-text); }

  .brand { display: flex; align-items: center; gap: 12px; }
  .brand__square {
    width: 34px; height: 34px; flex: none;
    border: 2px solid currentColor;
  }
  .brand__text { display: flex; flex-direction: column; }
  .brand__name {
    font-weight: 700; font-size: 13px; letter-spacing: 0.06em; text-transform: uppercase;
    white-space: nowrap;
  }
  .brand__tagline { font-weight: 700; font-size: 11.5px; margin-top: 3px; white-space: nowrap; }

  .card--front .brand { position: absolute; left: 150px; top: 38px; }

  .person {
    position: absolute; left: 70px; top: 118px; width: 150px; text-align: right;
  }
  .person__name { font-weight: 700; font-size: 17px; letter-spacing: 0.02em; }
  .person__title { font-size: 12.5px; color: var(--ink-soft); margin-top: 2px; }

  .divider {
    position: absolute; left: 243px; top: 112px; width: 1.5px; height: 74px;
    background: var(--ink);
  }

  .contacts {
    position: absolute; left: 262px; top: 114px; list-style: none;
  }
  .contacts__item {
    display: flex; align-items: center; gap: 9px;
    font-size: 13px; line-height: 22px; color: var(--ink); white-space: nowrap;
  }
  .contacts__icon { width: 12px; height: 12px; flex: none; fill: var(--ink); }

  .address-band {
    position: absolute; left: 0; right: 0; top: 212px; height: 40px;
    background: var(--card-black); color: var(--paper-text);
    display: flex; align-items: center; padding-left: 40px;
    font-size: 13px; letter-spacing: 0.01em;
  }

  .card--back .brand {
    position: absolute; left: 140px; top: 112px;
  }
  .card--back .brand__square { width: 44px; height: 44px; }
</style>
</head>
<body>
<main class="stage">

  <section class="card card--front" aria-label="Business card front">
    <div class="brand">
      <span class="brand__square" aria-hidden="true"></span>
      <div class="brand__text">
        <span class="brand__name">The Larchmont Fitters</span>
        <span class="brand__tagline">Built Right, Hung Straight</span>
      </div>
    </div>

    <div class="person">
      <p class="person__name">YOUR NAME</p>
      <p class="person__title">Your Title</p>
    </div>

    <div class="divider" aria-hidden="true"></div>

    <ul class="contacts">
      <li class="contacts__item">
        <svg class="contacts__icon" viewBox="0 0 24 24" aria-hidden="true"><path d="M6.6 10.8a15.1 15.1 0 0 0 6.6 6.6l2.2-2.2a1 1 0 0 1 1-.25 11.4 11.4 0 0 0 3.6.57 1 1 0 0 1 1 1V20a1 1 0 0 1-1 1A17 17 0 0 1 3 4a1 1 0 0 1 1-1h3.5a1 1 0 0 1 1 1c0 1.25.2 2.45.57 3.57a1 1 0 0 1-.25 1z"/></svg>
        <span>123-456-2100</span>
      </li>
      <li class="contacts__item">
        <svg class="contacts__icon" viewBox="0 0 24 24" aria-hidden="true"><path d="M2 5h20v14H2z M3.5 6.5 12 13l8.5-6.5" fill="none" stroke="#111" stroke-width="2"/></svg>
        <span>youremail@larchmontmail.com</span>
      </li>
      <li class="contacts__item">
        <svg class="contacts__icon" viewBox="0 0 24 24" aria-hidden="true"><circle cx="12" cy="12" r="10" fill="none" stroke="#111" stroke-width="2"/><path d="M2 12h20M12 2c3 3 3 17 0 20M12 2c-3 3-3 17 0 20" fill="none" stroke="#111" stroke-width="1.6"/></svg>
        <span>www.yourwebsite.com</span>
      </li>
    </ul>

    <div class="address-band">Your address, city, state, ZIP 0000</div>
  </section>

  <section class="card card--back" aria-label="Business card back">
    <div class="brand">
      <span class="brand__square" aria-hidden="true"></span>
      <div class="brand__text">
        <span class="brand__name">The Larchmont Fitters</span>
        <span class="brand__tagline">Built Right, Hung Straight</span>
      </div>
    </div>
  </section>

</main>
</body>
</html>
```